Flooring Company Stationery Design Project

I need Business card, presentation folder, letterhead and envelope design.
I want the design to show a lot of creativity and that it has a modern look but still professional.
The company has a retail store but we specialize in in-home shopping.

Design must have a "flooring" company style. Creativity is going to be the main thing we'll be looking for. We want something that will stand out of the competition.

We are a remodeling busines and we want to look like one but with a good look.

PLEASE USE FOLLOWING LINK FOR ANY PHOTOS NEEDED
http://www.velmorta.com/syndicate/logos/choose_brands.html
Updates

PLEASE USE ANY PHOTOS NEEDED FROM HERE

Target Market(s)

Our target customer are 35-50 years old and decision makers are usually women

Industry/Entity Type

Retail

Requirements
Must have
• Color red
PHOTOS NEEDED CAN BE USED FROM HERE

```html
<!DOCTYPE html>
<html lang="en">
<head>
<meta charset="utf-8">
<title>Plankwell Business Card</title>
<link rel="stylesheet" href="https://fonts.googleapis.com/css2?family=Jost:wght@400;500;700&display=swap">
<style>
  :root {
    --backdrop: #3a3a3a;
    --brand-red: #c81d2a;
    --brand-red-deep: #b3151f;
    --card-white: #f7f7f5;
    --text-grey: #6b6b6b;
    --rule-grey: #bdbdbd;
    --accent-teal: #1e8fa6;
    --accent-yellow: #e8b21c;
    --on-red: #ffffff;
  }
  * { margin: 0; padding: 0; box-sizing: border-box; }
  html, body { width: 1200px; height: 900px; overflow: hidden; }
  body {
    background: var(--backdrop);
    font-family: "Jost", "Futura", sans-serif;
    position: relative;
  }
  .card {
    position: absolute;
    left: 285px;
    width: 630px;
    height: 360px;
    border-radius: 22px;
    box-shadow: 0 10px 30px rgba(0,0,0,0.35);
  }
  .card--back {
    top: 50px;
    background: linear-gradient(135deg, var(--brand-red) 0%, var(--brand-red-deep) 100%);
    color: var(--on-red);
  }
  .card--front {
    top: 470px;
    background: var(--card-white);
    color: var(--text-grey);
  }

  /* back side */
  .back-brand {
    position: absolute;
    left: 0; right: 0; top: 122px;
    text-align: center;
  }
  .back-brand__name {
    font-size: 64px;
    font-weight: 700;
    letter-spacing: -1px;
    line-height: 1;
  }
  .back-brand__tagline {
    margin-top: 8px;
    font-size: 17px;
    font-weight: 500;
  }
  .back-web {
    position: absolute;
    left: 0; right: 0; bottom: 36px;
    text-align: center;
    font-size: 15px;
  }

  /* front side */
  .front-brand {
    position: absolute;
    left: 40px; top: 50px;
  }
  .front-brand__name {
    font-size: 46px;
    font-weight: 700;
    color: var(--brand-red);
    letter-spacing: -1px;
    line-height: 1;
  }
  .front-brand__tagline {
    margin-top: 4px;
    margin-left: 110px;
    font-size: 13px;
    font-weight: 500;
    color: var(--accent-teal);
  }
  .holder {
    position: absolute;
    right: 40px; top: 60px;
    text-align: right;
    width: 190px;
    border-bottom: 1px solid var(--rule-grey);
    padding-bottom: 6px;
  }
  .holder__name { font-size: 22px; font-weight: 500; color: var(--brand-red); line-height: 1.1; }
  .holder__role { font-size: 16px; color: var(--text-grey); }
  .web {
    position: absolute;
    right: 40px; top: 170px;
    font-size: 15px;
    color: var(--text-grey);
  }
  .divider {
    position: absolute;
    left: 40px; right: 40px; top: 196px;
    border-top: 1px solid var(--rule-grey);
  }
  .contact {
    position: absolute;
    left: 40px; top: 240px;
    list-style: none;
    font-size: 15px;
    color: var(--text-grey);
  }
  .contact__row { display: flex; align-items: center; gap: 6px; height: 24px; }
  .contact__row svg { width: 13px; height: 13px; fill: var(--accent-yellow); flex: none; }
  .contact__gap { width: 8px; }
</style>
</head>
<body>
  <section class="card card--back" aria-label="Card back">
    <div class="back-brand">
      <div class="back-brand__name">Plankwell</div>
      <div class="back-brand__tagline">Adding Value To Your Home</div>
    </div>
    <div class="back-web">www.plankwell.com</div>
  </section>

  <section class="card card--front" aria-label="Card front">
    <div class="front-brand">
      <div class="front-brand__name">Plankwell</div>
      <div class="front-brand__tagline">Adding Value To Your Home</div>
    </div>
    <div class="holder">
      <div class="holder__name">John Doe</div>
      <div class="holder__role">President</div>
    </div>
    <div class="web">www.plankwell.com</div>
    <div class="divider"></div>
    <ul class="contact">
      <li class="contact__row">
        <svg viewBox="0 0 16 16" aria-hidden="true"><path d="M8 0a5.5 5.5 0 0 0-5.5 5.5C2.5 10 8 16 8 16s5.5-6 5.5-10.5A5.5 5.5 0 0 0 8 0zm0 8a2.5 2.5 0 1 1 0-5 2.5 2.5 0 0 1 0 5z"/></svg>
        Suit 123, Your Street Cityname Country123456
      </li>
      <li class="contact__row">
        <svg viewBox="0 0 16 16" aria-hidden="true"><path d="M1 5c0-2 3-4 7-4s7 2 7 4v1h-4V4.5H5V6H1zM3 7h10l2 8H1z"/></svg>
        08 9000 4821
        <span class="contact__gap"></span>
        <svg viewBox="0 0 16 16" aria-hidden="true"><path d="M4 0h8a1 1 0 0 1 1 1v14a1 1 0 0 1-1 1H4a1 1 0 0 1-1-1V1a1 1 0 0 1 1-1zm1 2v8h6V2zm3 10a1.2 1.2 0 1 0 0 2.4A1.2 1.2 0 0 0 8 12z"/></svg>
        0488 000 735
      </li>
      <li class="contact__row">
        <svg viewBox="0 0 16 16" aria-hidden="true"><path d="M0 3h16v10H0zm1.5 1.2L8 9l6.5-4.8V4h-13z"/></svg>
        info@plankwell.com
      </li>
    </ul>
  </section>
</body>
</html>
```